Business Card Design with new logo

Dorian Pelleway 4172
E 118th St Dunmore, IL 61847
Cell: 217-555-0193
pellewayrestoration@mailvane.test

Classic Car Restoration Services Buy Sell Trade Consign

Dorian Pelleway 9698
Cell: 217-555-0193

```html
<!DOCTYPE html>
<html lang="en">
<head>
<meta charset="utf-8">
<title>Pelleway Restoration LLC – Business Card</title>
<link href="https://fonts.googleapis.com/css2?family=Arimo:wght@400;700&display=swap" rel="stylesheet">
<style>
  :root {
    --page-bg: #2a2a2a;
    --card-black: #050505;
    --card-white: #ffffff;
    --card-red: #b3161c;
    --card-red-dark: #8e0f14;
    --brand-navy: #1e2a38;
    --ink-light: #ffffff;
    --ink-soft: #f1c9ca;
    --divider: #0c0c0c;
  }
  * { margin: 0; padding: 0; box-sizing: border-box; }
  html, body { width: 1200px; height: 997px; overflow: hidden; }
  body {
    background: var(--page-bg);
    font-family: "Arimo", Arial, sans-serif;
    position: relative;
  }
  .card {
    position: absolute;
    width: 600px;
    height: 343px;
    border-radius: 22px;
    overflow: hidden;
    box-shadow: 0 14px 34px rgba(0,0,0,.45);
  }
  .card-back {
    left: 300px; top: 90px;
    background: var(--card-black);
    display: flex; align-items: center; justify-content: center; gap: 18px;
  }
  .card-back .brand-mark { width: 34px; height: 34px; border-radius: 50%; background: var(--ink-light); }
  .card-back .brand-name {
    color: var(--ink-light); font-weight: 700; font-size: 40px; letter-spacing: 2px;
    text-transform: uppercase;
  }
  .card-front {
    left: 300px; top: 520px;
    display: grid; grid-template-columns: 296px 8px 296px;
    background: var(--card-white);
  }
  .front-brand {
    display: flex; flex-direction: column; align-items: center; justify-content: center; gap: 14px;
    padding: 20px;
  }
  .front-brand .brand-mark { width: 26px; height: 26px; border-radius: 50%; background: var(--brand-navy); }
  .front-brand .brand-name {
    color: var(--brand-navy); font-weight: 700; font-size: 25px; letter-spacing: 1.5px;
    text-transform: uppercase; text-align: center; line-height: 1.25;
  }
  .front-divider { background: var(--divider); position: relative; }
  .front-divider::after {
    content: ""; position: absolute; left: -3px; top: 44px;
    width: 14px; height: 14px; background: var(--divider); transform: rotate(45deg);
  }
  .front-info {
    background: linear-gradient(135deg, var(--card-red), var(--card-red-dark));
    color: var(--ink-light);
    padding: 36px 22px 0 28px;
  }
  .person-name { font-weight: 700; font-size: 17px; letter-spacing: .6px; text-transform: uppercase; color: var(--divider); }
  .person-role { font-size: 13px; color: var(--divider); margin-top: 2px; }
  .service-line { font-size: 10.5px; text-transform: uppercase; letter-spacing: .4px; color: var(--ink-soft); margin-top: 30px; }
  .address { font-size: 12.5px; margin-top: 4px; line-height: 1.35; }
  .contact-list { list-style: none; margin-top: 22px; }
  .contact-list li { display: flex; align-items: center; gap: 10px; font-size: 12.5px; margin-bottom: 10px; }
  .contact-icon {
    width: 18px; height: 18px; border-radius: 50%; background: var(--ink-light);
    display: flex; align-items: center; justify-content: center; flex: none;
  }
  .contact-icon svg { width: 11px; height: 11px; fill: var(--card-red); }
  .email { font-size: 12px; white-space: nowrap; }
</style>
</head>
<body>
  <section class="card card-back" aria-label="Card back">
    <span class="brand-mark"></span>
    <span class="brand-name">Pelleway</span>
  </section>

  <section class="card card-front" aria-label="Card front">
    <div class="front-brand">
      <span class="brand-mark"></span>
      <span class="brand-name">Pelleway<br>Restoration LLC</span>
    </div>
    <div class="front-divider"></div>
    <div class="front-info">
      <p class="person-name">Dorian Pelleway</p>
      <p class="person-role">Office Manager</p>
      <p class="service-line">Classic Car Restoration Services</p>
      <p class="address">4172 E 118th St<br>Dunmore, IL 61847</p>
      <ul class="contact-list">
        <li>
          <span class="contact-icon"><svg viewBox="0 0 24 24"><path d="M6.6 10.8a15.1 15.1 0 0 0 6.6 6.6l2.2-2.2a1 1 0 0 1 1-.25 11.4 11.4 0 0 0 3.6.57 1 1 0 0 1 1 1V20a1 1 0 0 1-1 1A17 17 0 0 1 3 4a1 1 0 0 1 1-1h3.5a1 1 0 0 1 1 1c0 1.25.2 2.45.57 3.6a1 1 0 0 1-.25 1z"/></svg></span>
          <span>217-555-0193</span>
        </li>
        <li>
          <span class="contact-icon"><svg viewBox="0 0 24 24"><path d="M2 5h20v14H2z M4 7v.5l8 5 8-5V7l-8 5z" fill-rule="evenodd"/></svg></span>
          <span class="email">pellewayrestoration@mailvane.test</span>
        </li>
      </ul>
    </div>
  </section>
</body>
</html>
```